Mead Label for craft mead bottle

Need a better label for our Garrow's Hollow Mead. It's Plum Mead, and who doesn't have a Garrows Hollow? Need all information from the current label: government warning, alcohol content, volume statement - 500 Ml, contains sulfite message, produced and bottles by statement, Tindle Brews and www.tindlebrews.example, Garrow's Hollow Mead, logo (though it could be smaller with a fanciful character representing a Garrows hollow), room for a bar code. Label should be 4x6.
Updates

Project Deadline Extended Reason: I have been sick all weekend, and working off an iPhone. It's pretty hard to view the label submissions and provide comments on a 3" screen. Added Monday, October 23, 2017

Target Market(s)

Craft beer and craft spirit croud. Mead is slightly more targeted to women then men.

Industry/Entity Type

Brewery

Colors

Designer to choose colors to be used in the design.

Requirements
Must have
• Needs to stand out on a shelf
Nice to have
• Mead background... Mead is probably the oldest alcoholic beverage made by man. Some version of it exists in just about every culture. It is fermented honey. In this case, honey and plum juice fermented together.
Should not have
• This is craft mead, not the stuff most people had when they were under 18 at a renaissance fair. Think fruity cocktail.

```html
<!DOCTYPE html>
<html lang="en">
<head>
<meta charset="utf-8">
<title>Garrow's Hollow Mead – Label</title>
<link href="https://fonts.googleapis.com/css2?family=Oswald:wght@700&family=Lato:wght@400;700&display=swap" rel="stylesheet">
<style>
  :root {
    --plum: #8e1d5c;
    --plum-dark: #6e1447;
    --plum-light: #b42672;
    --label-white: #f7f7f7;
    --backdrop: #d9dde0;
    --ink: #8a1a58;
  }
  * { box-sizing: border-box; margin: 0; padding: 0; }
  html, body { width: 1200px; height: 960px; overflow: hidden; }
  body {
    background: radial-gradient(ellipse at center, #eef0f2 0%, var(--backdrop) 75%);
    font-family: 'Lato', sans-serif;
    position: relative;
  }
  .label {
    position: absolute;
    top: 156px;
    width: 252px;
    height: 640px;
    background: var(--label-white);
    border-radius: 6px;
    overflow: hidden;
    box-shadow: 0 10px 24px rgba(0,0,0,0.12);
  }
  .label--front { left: 258px; }
  .label--back { left: 690px; }

  .band { position: absolute; left: 0; width: 100%; background: var(--plum); }

  /* Front */
  .front-field {
    position: absolute; left: 0; top: 72px; width: 100%; height: 496px;
    background: linear-gradient(90deg, var(--plum-dark) 0%, var(--plum) 55%, var(--plum-light) 100%);
  }
  .badge-stripe {
    position: absolute; left: 0; top: 340px; width: 100%; height: 64px;
    background: var(--label-white);
  }
  .product-name {
    position: absolute; left: 0; top: 88px; width: 100%;
    text-align: center; color: #fff;
    font-family: 'Oswald', sans-serif; font-weight: 700;
    text-transform: uppercase; line-height: 1.08;
  }
  .product-name .line-1 { display: block; font-size: 38px; }
  .product-name .line-2 { display: block; font-size: 38px; }
  .product-name .line-3 { display: block; font-size: 62px; line-height: 1; }
  .badge {
    position: absolute; left: 10px; top: 260px; width: 232px; height: 232px;
  }
  .badge .brand-name {
    position: absolute; left: 0; top: 150px; width: 100%;
    text-align: center; color: #fff;
    font-family: 'Lato', sans-serif; font-weight: 700; font-size: 22px;
  }
  .strength {
    position: absolute; left: 0; top: 500px; width: 100%;
    text-align: center; color: #fff; font-size: 20px; line-height: 1.35;
  }

  /* Back */
  .back-content {
    position: absolute; left: 0; top: 96px; width: 100%;
    text-align: center; color: var(--ink);
  }
  .back-brand { font-weight: 700; font-size: 23px; }
  .back-url { font-weight: 700; font-size: 16px; margin-top: 4px; }
  .back-city { font-weight: 700; font-size: 17px; margin-top: 2px; }
  .producer { font-size: 13.5px; line-height: 1.35; margin: 38px 14px 0; }
  .warning-title {
    font-weight: 700; font-size: 15.5px; margin-top: 42px;
    text-decoration: underline; text-underline-offset: 3px;
  }
  .warning-text { font-size: 11px; line-height: 1.6; margin: 14px 4px 0; letter-spacing: -0.2px; }
  .warning-text p + p { margin-top: 6px; }
  .sulfites { font-weight: 700; font-size: 14px; margin-top: 28px; }
</style>
</head>
<body>

  <section class="label label--front" aria-label="Front label">
    <div class="band" style="top:42px;height:8px;"></div>
    <div class="front-field"></div>
    <div class="badge-stripe"></div>
    <h1 class="product-name">
      <span class="line-1">Garrow's</span>
      <span class="line-2">Hollow</span>
      <span class="line-3">Mead</span>
    </h1>
    <div class="badge">
      <svg width="232" height="232" viewBox="0 0 232 232">
        <circle cx="116" cy="116" r="114" fill="var(--label-white)"/>
        <circle cx="116" cy="116" r="102" fill="#5a1a38" role="img" aria-label="Brewery mascot illustration: hooded figure with wheat sprigs"/>
      </svg>
      <div class="brand-name">Tindle Brews</div>
    </div>
    <p class="strength">ALC. 13% BY VOL.<br>500 ML</p>
    <div class="band" style="top:582px;height:14px;"></div>
  </section>

  <section class="label label--back" aria-label="Back label">
    <div class="band" style="top:42px;height:12px;"></div>
    <div class="band" style="top:76px;height:2px;"></div>
    <div class="back-content">
      <h2 class="back-brand">TINDLE BREWS</h2>
      <p class="back-url">www.tindlebrews.example</p>
      <p class="back-city">Fairmont, CA</p>
      <p class="producer">Produced and bottled by Bayline Craft Cellars Inc. dba Tindle Brews Fairmont, CA</p>
      <p class="warning-title">GOVERNMENT WARNING:</p>
      <div class="warning-text">
        <p>(1) According to the Surgeon General, women should not drink alcoholic beverages during pregnancy because of the risk of birth defects.</p>
        <p>(2) Consumption of alcoholic beverages impairs your ability to drive a car or operate machinery, and may cause health problems.</p>
      </div>
      <p class="sulfites">Contains Sulfites</p>
    </div>
    <div class="band" style="top:553px;height:4px;"></div>
    <div class="band" style="top:578px;height:16px;"></div>
  </section>

</body>
</html>
```